Need an postcard design to promote a website

I need a postcard design to promote a website.
The website is about accesible skiing-facilities in Sweden. Like Sitski, Skicart, Biski and other helping equipment for people with a disability.
You can on the site search about different ski-facilities and ski-resorts and see what level of accessibility they have. The level is an internal ranking-system that give a score to the facilitiy and is presented in three levels. You get quick info, about the facility and how it is ranked. This postcard is thought to be mailed to selected people and organisations that we think of, could have use for the website.
Background: I have myself worked many years in the Parasport-Community. And was one of the persons that initiated the project. It was given support from the Lakeshore Civic Endowment. I can do design myself (see vykort.korr.pdf - I have done something but I am not pleased with what I have done, but there you get a feel for it. The text is all good.)
Format 165 x 115 mm. It will be printed in CMYK.

Time is short, I hope I can find a talented designer to help me put an postcard design together. Thanks.

Target Market(s)

Nonprofit, individuals.

Industry/Entity Type

Non Profit

Requirements
Must have
• The feel of a postcard, with everything that should be there, except the stamp. But ofcourse an area for it and the adress.
Nice to have
• The signature, in some nice handwritten font.
• The map somehow.

```html
<!DOCTYPE html>
<html lang="sv">
<head>
<meta charset="utf-8">
<title>Snowreach – vykort</title>
<link href="https://fonts.googleapis.com/css2?family=Courgette&family=Oswald:wght@500&family=Mrs+Saint+Delafield&display=swap" rel="stylesheet">
<style>
  :root{
    --bg:#bdbdbd;
    --teal:#3dbfb8;
    --teal-dark:#2a9f99;
    --lavender:#c9c8d6;
    --snow:#eeeeef;
    --snow-shade:#dcdce2;
    --ink:#1d1d1f;
    --charcoal:#3a3a3c;
    --line:#8e8e94;
  }
  *{box-sizing:border-box;margin:0;padding:0}
  html,body{width:1200px;height:802px;overflow:hidden;background:var(--bg)}
  .stage{position:relative;width:1200px;height:802px;display:flex;gap:40px;align-items:center;justify-content:center}
  .postcard{position:relative;width:560px;height:390px;background:linear-gradient(180deg,var(--snow) 0%,var(--snow-shade) 100%);box-shadow:0 6px 18px rgba(0,0,0,.22);overflow:hidden}

  /* Front */
  .front-sky{position:absolute;left:0;top:0;width:100%;height:170px;background:var(--lavender)}
  .front-snow{position:absolute;left:0;top:150px;width:100%;height:240px;background:linear-gradient(180deg,#e4e4ea,#d2d3da)}
  .brand{position:absolute;left:150px;top:60px;display:flex;align-items:center;gap:12px}
  .brand-name{font-family:'Oswald',sans-serif;font-weight:500;font-size:46px;letter-spacing:1px;color:var(--charcoal);line-height:1}
  .brand-dot{width:38px;height:38px;border-radius:50%;background:var(--teal)}
  .photo{position:absolute;box-shadow:0 2px 6px rgba(0,0,0,.25)}
  .photo-strip-1{left:230px;top:130px;width:140px;height:86px;background:linear-gradient(160deg,#3d4a33,#6e7a5c 55%,#e8ebf0 56%)}
  .photo-strip-2{left:385px;top:120px;width:140px;height:96px;background:linear-gradient(170deg,#55606c,#9aa5b4 50%,#f1f3f6 51%)}
  .photo-main{left:40px;top:170px;width:200px;height:140px;background:linear-gradient(165deg,#5a6470 0%,#8c95a0 45%,#f2f3f6 46%,#dfe2e8 100%)}
  .teal-band{position:absolute;left:0;bottom:0;width:100%;height:66px;background:linear-gradient(90deg,var(--teal),var(--teal-dark))}
  .band-text{position:absolute;left:24px;bottom:10px;width:520px;font-family:'Courgette',cursive;font-size:16px;line-height:1.3;color:#fff;text-align:center}

  /* Back */
  .back-top{position:absolute;left:0;top:0;width:100%;height:52px;background:var(--lavender)}
  .message{position:absolute;left:30px;top:78px;width:280px;font-family:'Courgette',cursive;font-size:13.5px;line-height:1.45;color:var(--ink)}
  .message p+p{margin-top:10px}
  .sign-off{position:absolute;left:30px;top:298px;font-family:'Courgette',cursive;font-size:13.5px;color:var(--ink)}
  .signature{position:absolute;left:34px;top:318px;font-family:'Mrs Saint Delafield',cursive;font-size:36px;color:var(--ink)}
  .portrait{position:absolute;left:232px;top:282px;width:72px;height:78px;background:#fff;padding:5px;box-shadow:0 1px 4px rgba(0,0,0,.25)}
  .portrait span{display:block;width:100%;height:100%;background:linear-gradient(180deg,#e6e8ec,#9aa3b4)}
  .divider{position:absolute;left:326px;top:74px;width:1px;height:250px;background:var(--line)}
  .address-lines{position:absolute;left:346px;top:190px;width:186px}
  .address-lines span{display:block;height:1px;background:var(--line);margin-bottom:40px}
</style>
</head>
<body>
<main class="stage">
  <section class="postcard postcard-front" aria-label="Vykortets framsida">
    <div class="front-sky"></div>
    <div class="front-snow" role="img" aria-label="Snötäckt skidbacke med lift"></div>
    <div class="brand">
      <span class="brand-name">Snowreach</span>
      <span class="brand-dot"></span>
    </div>
    <div class="photo photo-strip-1" role="img" aria-label="Skidåkare i orange väst i backen"></div>
    <div class="photo photo-strip-2" role="img" aria-label="Instruktörer med skidutrustning bland träden"></div>
    <div class="photo photo-main" role="img" aria-label="Instruktör kör en sitski nedför backen"></div>
    <div class="teal-band">
      <p class="band-text">Sveriges första kartläggning av skidanläggningar för personer med funktionsnedsättning</p>
    </div>
  </section>

  <section class="postcard postcard-back" aria-label="Vykortets baksida">
    <div class="back-top"></div>
    <div class="message">
      <p>Hej!</p>
      <p>Känslan att åka ner för en snöklädd backe är bland det bästa som finns. Den känslan ska alla kunna ta del av oavsett fysiska förutsättningar. Därför uppskattar jag initiativet snowreach.se där jag kan se hur tillgängligheten på skidanläggningarna ser ut.</p>
    </div>
    <p class="sign-off">Vänliga hälsningar</p>
    <p class="signature">Elias Marklund</p>
    <div class="portrait" role="img" aria-label="Porträttfoto av avsändaren"><span></span></div>
    <div class="divider"></div>
    <div class="address-lines"><span></span><span></span><span></span></div>
  </section>
</main>
</body>
</html>
```